Website for PeakStride Functional Training

We would like to launch a website for our boutique gym, PeakStride Functional Training. We'd like the website to have a lot of lime green which is one of our colors in our logo. The website will have a description of our workouts, membership, free trial class and location information.

Target Market(s)

Fitness enthusiasts, health conscious people, target ages 20-65, people looking to get fit and healthy, people looking to lose weight

Industry/Entity Type

Gym

Coding

Number of Pages Required

1 page

Font styles to use
Serif

Colors
9ccb3b
34a7d8

Requirements
Must have
• A lot of lime green to match our logo. Let the website be fun, eye catchy. Our phone number which is 614-287-9153 to be easily dialed directly from our website.
Nice to have
• We would like to include this verbiage:
• -The Most FUN 1 hour workout
• -Affordable personal training/group training
• -Individualized workout programs
• -FUN workouts delivering results
• -Turn ON fat burn-The Most FUN 1 hour workout
• -Turn ON fat burning "EPOC" after burn
• We want our website to be easily seen on smart phones, iPads, Androids
Should not have
• Font that is hard on the eyes

```html
<!DOCTYPE html>
<html lang="en">
<head>
<meta charset="utf-8">
<title>PeakStride Functional Training – Responsive Layouts</title>
<link href="https://fonts.googleapis.com/css2?family=Tinos:wght@400;700&family=Roboto:wght@300&display=swap" rel="stylesheet">
<style>
:root{
  --lime:#9ccb3b;
  --sky:#34a7d8;
  --bar:#333333;
  --ink:#3a3a3a;
  --paper:#ffffff;
  --bg:#ffffff;
  --hero-a:#5b5f63;
  --hero-b:#2d3033;
}
*{box-sizing:border-box;margin:0;padding:0}
html,body{width:1200px;height:1200px;overflow:hidden;background:var(--bg)}
body{font-family:"Tinos",serif;color:var(--ink)}
.stage{position:absolute;left:0;top:0;width:1010px;height:1010px;transform:scale(1.17);transform-origin:0 0}
.screen{position:absolute;background:var(--paper);overflow:hidden}
.abs{position:absolute}
.device-label{position:absolute;font-family:"Roboto",sans-serif;font-weight:300;font-size:22px;color:#333;text-align:center}
/* top bar */
.topbar{position:absolute;left:0;top:0;width:100%;background:var(--bar);color:#fff;font-size:6px;display:flex;align-items:center;padding:0 8px;gap:8px}
.open-dot{display:inline-block;width:6px;height:6px;border-radius:50%;background:var(--lime);margin-right:4px;vertical-align:middle}
.social{position:absolute;display:flex;gap:4px}
.social i{display:block;width:7px;height:7px;border-radius:50%;background:#fff}
/* brand */
.brand{position:absolute;font-family:"Tinos",serif;font-weight:700;color:var(--lime);letter-spacing:.5px;white-space:nowrap}
.nav{position:absolute;display:flex;gap:5px;font-size:6.4px;color:var(--sky);text-transform:uppercase}
/* hero */
.hero{position:absolute;left:0;width:100%;background:linear-gradient(135deg,var(--hero-a),var(--hero-b))}
.hero-arrow{position:absolute;width:14px;height:14px;border-radius:3px;background:rgba(0,0,0,.35);color:#fff;font-size:10px;line-height:14px;text-align:center;font-family:"Roboto",sans-serif}
.hero-copy{position:absolute;left:0;width:100%;text-align:center;color:#fff;white-space:nowrap}
.hero-copy .most{vertical-align:baseline}
.hero-copy .fun{color:var(--lime)}
.hero-copy .hour{display:inline-block;background:rgba(40,40,40,.6);padding:0 8px}
/* bands */
.band{position:absolute;left:0;width:100%;background:var(--sky);color:#fff;text-align:center;white-space:nowrap}
.lorem{position:absolute;font-size:5.6px;line-height:1.4;color:#444;text-align:justify}
.photo{position:absolute}
.green-fill{position:absolute;background:var(--lime)}
.hex{position:absolute}
.feature-cap{position:absolute;font-size:5.4px;line-height:1.3;text-align:center;color:#444}
.footer{position:absolute;left:0;width:100%;background:var(--lime);color:#fff;text-align:center;line-height:1.35}
.contact-ico{position:absolute;text-align:center;font-size:5.5px;color:#333}
.field-label{position:absolute;font-size:5px;color:#444}
.field{position:absolute;border:1px solid #ddd;background:#fff}
.send{position:absolute;background:var(--lime);color:#fff;font-size:5.5px;text-align:center}
</style>
</head>
<body>
<svg width="0" height="0" style="position:absolute">
  <defs>
    <symbol id="hex-trainer" viewBox="0 0 60 60">
      <polygon points="16,3 44,3 58,30 44,57 16,57 2,30" fill="currentColor"/>
      <circle cx="30" cy="19" r="5" fill="none" stroke="#fff" stroke-width="2.2"/>
      <path d="M22 42 v-9 q8-6 16 0 v9" fill="none" stroke="#fff" stroke-width="2.2"/>
      <rect x="33" y="37" width="10" height="7" fill="none" stroke="#fff" stroke-width="2"/>
    </symbol>
    <symbol id="hex-plan" viewBox="0 0 60 60">
      <polygon points="16,3 44,3 58,30 44,57 16,57 2,30" fill="currentColor"/>
      <rect x="16" y="20" width="10" height="6" fill="none" stroke="#fff" stroke-width="2"/>
      <rect x="34" y="20" width="10" height="6" fill="none" stroke="#fff" stroke-width="2"/>
      <rect x="21" y="32" width="18" height="9" fill="none" stroke="#fff" stroke-width="2"/>
      <path d="M26 23 h8 M30 26 v6" stroke="#fff" stroke-width="2"/>
    </symbol>
    <symbol id="hex-flex" viewBox="0 0 60 60">
      <polygon points="16,3 44,3 58,30 44,57 16,57 2,30" fill="currentColor"/>
      <path d="M14 34 q2-12 10-12 q6 0 6 6 q0-6 6-6 q8 0 10 12 l-6 6 q-10-6-20 0 z" fill="none" stroke="#fff" stroke-width="2.2" stroke-linejoin="round"/>
    </symbol>
    <symbol id="hex-scale" viewBox="0 0 60 60">
      <polygon points="16,3 44,3 58,30 44,57 16,57 2,30" fill="currentColor"/>
      <rect x="17" y="17" width="26" height="26" rx="4" fill="none" stroke="#fff" stroke-width="2.2"/>
      <path d="M22 26 h16" stroke="#fff" stroke-width="2.2"/>
      <path d="M30 22 v4" stroke="#fff" stroke-width="2"/>
    </symbol>
    <symbol id="ico-phone" viewBox="0 0 24 24">
      <path d="M6 2 l4 4 -2.5 2.5 q2 4.5 8 8 L18 14 l4 4 -3 3 Q8 20 3 5 z" fill="currentColor"/>
    </symbol>
    <symbol id="ico-pin" viewBox="0 0 24 24">
      <path d="M12 2 a7 7 0 0 1 7 7 c0 5 -7 13 -7 13 s-7 -8 -7 -13 a7 7 0 0 1 7 -7z" fill="currentColor"/>
      <circle cx="12" cy="9" r="2.6" fill="#fff"/>
    </symbol>
    <symbol id="ico-mail" viewBox="0 0 24 24">
      <rect x="2" y="5" width="20" height="14" fill="currentColor"/>
      <path d="M2 5 l10 8 10-8 M2 19 l8-7 M22 19 l-8-7" stroke="#fff" stroke-width="1.4" fill="none"/>
    </symbol>
  </defs>
</svg>

<main class="stage">

  <!-- ============ COMPUTER ============ -->
  <section class="screen screen--desktop" style="left:20px;top:15px;width:335px;height:925px;">
    <div class="topbar" style="height:26px;align-items:flex-start;padding-top:9px;font-size:5px;">
      <span><span class="open-dot"></span>NOW OPEN</span>
      <span>MON - SAT &nbsp;8AM - 11PM &nbsp;| &nbsp;SUN &nbsp;10AM - 8PM</span>
    </div>
    <a class="abs" href="tel:6142879153" style="right:24px;top:5px;color:#fff;font-size:5px;text-decoration:none;">
      <svg width="7" height="7" style="vertical-align:middle;color:#fff"><use href="#ico-phone"/></svg> CALL US 614-287-9153</a>
    <div class="social" style="right:24px;top:15px;"><i></i><i></i><i></i><i></i></div>

    <div class="brand" style="left:22px;top:30px;font-size:13px;">PeakStride</div>
    <nav class="nav" style="left:127px;top:36px;font-size:6px;"><span>Home</span><span>Get Started</span><span>Trainers</span><span>Services</span><span>Contact</span></nav>

    <div class="hero" style="top:53px;height:168px;" role="img" aria-label="Photo of two athletes training with kettlebells in a concrete studio"></div>
    <div class="hero-arrow" style="left:8px;top:122px;">‹</div>
    <div class="hero-arrow" style="right:8px;top:122px;">›</div>
    <div class="hero-copy" style="left:62px;width:240px;top:138px;">
      <span class="most" style="font-size:15px;">THE MOST</span> <span class="fun" style="font-size:28px;">FUN</span><br>
      <span class="hour" style="font-size:9px;margin-left:20px;">1 HOUR WORKOUT</span>
    </div>

    <div class="green-fill" style="left:0;top:221px;width:335px;height:704px;"></div>
    <div class="abs" style="left:18px;top:195px;width:299px;height:688px;background:#fff;"></div>

    <svg class="hex" style="left:44px;top:208px;width:36px;height:36px;color:var(--sky)"><use href="#hex-trainer"/></svg>
    <svg class="hex" style="left:116px;top:208px;width:36px;height:36px;color:var(--lime)"><use href="#hex-plan"/></svg>
    <svg class="hex" style="left:189px;top:208px;width:36px;height:36px;color:var(--sky)"><use href="#hex-flex"/></svg>
    <svg class="hex" style="left:261px;top:208px;width:36px;height:36px;color:var(--sky)"><use href="#hex-scale"/></svg>
    <div class="feature-cap" style="left:24px;top:251px;width:76px;">Affordable Personal<br>Training/Group Training</div>
    <div class="feature-cap" style="left:96px;top:251px;width:76px;">Individualized<br>Workout Programs</div>
    <div class="feature-cap" style="left:169px;top:251px;width:76px;">FUN Workouts<br>Delivering Results</div>
    <div class="feature-cap" style="left:241px;top:251px;width:76px;">Turn ON Fat Burning<br>"EPOC" After Burn</div>

    <div class="band" style="top:291px;height:21px;font-size:10px;line-height:21px;">GET STARTED</div>
    <div class="photo" style="left:36px;top:322px;width:127px;height:84px;background:linear-gradient(135deg,#e9ecef,#c9cfd4);" role="img" aria-label="Photo of a woman doing a squat stretch"></div>
    <p class="lorem" style="left:180px;top:341px;width:118px;">Lorem ipsum dolor sit amet, consectetur adipiscing elit. Cras pellentesque, ante vitae bibendum porttitor, tellus augue mattis lacus, ut tristique sem neque et lacus. Vestibulum non urna ultricies, tristique mauris in, vehicula mi.</p>

    <div class="band" style="top:417px;height:21px;font-size:10px;line-height:21px;">TRAINERS</div>
    <div class="photo" style="left:36px;top:448px;width:127px;height:80px;background:linear-gradient(135deg,#8a96a3,#c7583f);" role="img" aria-label="Photo of two trainers in a gym"></div>
    <p class="lorem" style="left:180px;top:468px;width:118px;">Lorem ipsum dolor sit amet, consectetur adipiscing elit. Cras pellentesque, ante vitae bibendum porttitor, tellus augue mattis lacus, ut tristique sem neque et lacus. Vestibulum non urna ultricies, tristique mauris in, vehicula mi.</p>

    <div class="band" style="top:540px;height:21px;font-size:10px;line-height:21px;">SERVICES</div>
    <div class="photo" style="left:36px;top:573px;width:127px;height:85px;background:linear-gradient(135deg,#d9dde0,#9aa2a8);" role="img" aria-label="Photo of a group cycling class"></div>
    <p class="lorem" style="left:180px;top:594px;width:118px;">Lorem ipsum dolor sit amet, consectetur adipiscing elit. Cras pellentesque, ante vitae bibendum porttitor, tellus augue mattis lacus, ut tristique sem neque et lacus. Vestibulum non urna ultricies, tristique mauris in, vehicula mi.</p>

    <div class="band" style="top:670px;height:21px;font-size:10px;line-height:21px;">CONTACT</div>
    <div class="photo" style="left:32px;top:706px;width:136px;height:70px;background:linear-gradient(135deg,#e8e2cf,#b9cbe0);" role="img" aria-label="Street map showing the gym location"></div>
    <p class="abs" style="left:32px;top:784px;font-size:5px;color:#444;">Address<br>48 Harbor Ln, Seaview, FL, 32000</p>
    <span class="field-label" style="left:183px;top:702px;">Name</span>
    <div class="field" style="left:183px;top:709px;width:119px;height:8px;"></div>
    <span class="field-label" style="left:183px;top:722px;">E-mail</span>
    <div class="field" style="left:183px;top:729px;width:119px;height:8px;"></div>
    <span class="field-label" style="left:183px;top:742px;">Message</span>
    <div class="field" style="left:183px;top:749px;width:119px;height:86px;"></div>
    <div class="send" style="left:226px;top:847px;width:33px;height:10px;line-height:10px;">SEND</div>

    <p class="abs" style="left:0;top:901px;width:335px;text-align:center;font-size:4.2px;color:#fff;line-height:1.4;">© 2017 peakstride.com, LLC. All rights reserved. peakstride.com is a trademark of peakstride.com, LLC.<br>© peakstride.com, 48 Harbor Ln, Seaview, FL, 32000</p>
  </section>
  <div class="device-label" style="left:20px;top:943px;width:335px;">Computer</div>

  <!-- ============ TABLET ============ -->
  <section class="screen screen--tablet" style="left:385px;top:15px;width:328px;height:925px;">
    <div class="topbar" style="height:19px;font-size:6.4px;"><span><span class="open-dot"></span>NOW OPEN</span></div>
    <div class="social" style="right:20px;top:6px;"><i></i><i></i><i></i><i></i></div>

    <div class="abs" style="left:18px;top:36px;width:11px;height:8px;border-top:2px solid #333;border-bottom:2px solid #333;"><div style="margin-top:1px;height:2px;background:#333"></div></div>
    <div class="brand" style="left:0;width:328px;text-align:center;top:26px;font-size:19px;">PeakStride</div>
    <a href="tel:6142879153" class="abs" style="right:18px;top:33px;color:#333;"><svg width="12" height="12"><use href="#ico-phone"/></svg></a>

    <div class="hero" style="top:63px;height:165px;background:linear-gradient(135deg,#6f8ea0,#2f4450);" role="img" aria-label="Photo of a man stretching on a wet city waterfront"></div>
    <div class="hero-arrow" style="left:18px;top:138px;background:rgba(0,0,0,.2)">‹</div>
    <div class="hero-arrow" style="right:18px;top:138px;background:rgba(0,0,0,.2)">›</div>
    <div class="hero-copy" style="top:164px;">
      <span class="most" style="font-size:15px;">THE MOST</span> <span class="fun" style="font-size:28px;">FUN</span><br>
      <span class="hour" style="font-size:9px;">1 HOUR WORKOUT</span>
    </div>

    <svg class="hex" style="left:126px;top:241px;width:74px;height:70px;color:var(--lime)"><use href="#hex-trainer"/></svg>
    <div class="band" style="top:313px;height:17px;font-size:9px;line-height:17px;">Affordable Personal Training/Group Training</div>
    <p class="lorem" style="left:52px;top:339px;width:224px;">Lorem ipsum dolor sit amet, consectetur adipiscing elit. Cras pellentesque, ante vitae bibendum porttitor, tellus augue mattis lacus, ut tristique sem neque et lacus.</p>

    <svg class="hex" style="left:122px;top:386px;width:74px;height:70px;color:var(--lime)"><use href="#hex-plan"/></svg>
    <div class="band" style="top:461px;height:17px;font-size:9px;line-height:17px;">Individualized Workout Programs</div>
    <p class="lorem" style="left:52px;top:485px;width:224px;">Lorem ipsum dolor sit amet, consectetur adipiscing elit. Cras pellentesque, ante vitae bibendum porttitor, tellus augue mattis lacus, ut tristique sem neque et lacus.</p>

    <svg class="hex" style="left:122px;top:533px;width:74px;height:70px;color:var(--lime)"><use href="#hex-flex"/></svg>
    <div class="band" style="top:608px;height:17px;font-size:9px;line-height:17px;">FUN Workouts Delivering Results</div>
    <p class="lorem" style="left:52px;top:633px;width:224px;">Lorem ipsum dolor sit amet, consectetur adipiscing elit. Cras pellentesque, ante vitae bibendum porttitor, tellus augue mattis lacus, ut tristique sem neque et lacus.</p>

    <svg class="hex" style="left:122px;top:681px;width:74px;height:70px;color:var(--lime)"><use href="#hex-scale"/></svg>
    <div class="band" style="top:756px;height:17px;font-size:9px;line-height:17px;">Turn ON Fat Burning "EPOC" After Burn</div>
    <p class="lorem" style="left:52px;top:780px;width:224px;">Lorem ipsum dolor sit amet, consectetur adipiscing elit. Cras pellentesque, ante vitae bibendum porttitor, tellus augue mattis lacus, ut tristique sem neque et lacus.</p>

    <div class="contact-ico" style="left:112px;top:830px;width:40px;"><svg width="14" height="16" style="color:#222"><use href="#ico-pin"/></svg><br>FIND US</div>
    <div class="contact-ico" style="left:162px;top:832px;width:46px;"><svg width="18" height="14" style="color:#222"><use href="#ico-mail"/></svg><br>E-MAIL US</div>

    <div class="footer" style="top:870px;height:55px;padding-top:16px;font-size:5.4px;">© 2017 peakstride.com, LLC. All rights reserved.<br>peakstride.com is a trademark of peakstride.com, LLC.<br>© peakstride.com, 48 Harbor Ln, Seaview, FL, 32000</div>
  </section>
  <div class="device-label" style="left:385px;top:943px;width:328px;">Tablets</div>

  <!-- ============ SMARTPHONE ============ -->
  <section class="screen screen--phone" style="left:743px;top:15px;width:244px;height:938px;">
    <div class="topbar" style="height:27px;font-size:7px;"><span><span class="open-dot"></span>NOW OPEN</span></div>
    <div class="social" style="right:14px;top:9px;gap:6px;"><i style="width:9px;height:9px"></i><i style="width:9px;height:9px"></i><i style="width:9px;height:9px"></i><i style="width:9px;height:9px"></i></div>

    <div class="abs" style="left:14px;top:38px;width:15px;height:12px;border-top:2.5px solid #333;border-bottom:2.5px solid #333;"><div style="margin-top:2px;height:2.5px;background:#333"></div></div>
    <div class="brand" style="left:0;width:244px;text-align:center;top:33px;font-size:20px;">PeakStride</div>
    <a href="tel:6142879153" class="abs" style="right:14px;top:36px;color:#333;"><svg width="16" height="16"><use href="#ico-phone"/></svg></a>

    <div class="hero" style="top:74px;height:268px;background:linear-gradient(135deg,#9fb4c6,#3e4f5e);" role="img" aria-label="Photo of a woman stretching on a bridge"></div>
    <div class="hero-arrow" style="left:16px;top:196px;width:22px;height:22px;line-height:22px;font-size:16px;background:rgba(0,0,0,.3)">‹</div>
    <div class="hero-arrow" style="right:16px;top:196px;width:22px;height:22px;line-height:22px;font-size:16px;background:rgba(0,0,0,.3)">›</div>
    <div class="hero-copy" style="top:238px;">
      <span class="most" style="font-size:17px;">THE MOST</span> <span class="fun" style="font-size:34px;">FUN</span><br>
      <span class="hour" style="font-size:11px;">1 HOUR WORKOUT</span>
    </div>

    <svg class="hex" style="left:92px;top:355px;width:60px;height:56px;color:var(--lime)"><use href="#hex-trainer"/></svg>
    <div class="band" style="top:414px;height:15px;font-size:8px;line-height:15px;">Affordable Personal Training/Group Training</div>
    <p class="lorem" style="left:30px;top:436px;width:184px;">Lorem ipsum dolor sit amet, consectetur adipiscing elit. Cras pellentesque, ante vitae bibendum porttitor, tellus augue mattis lacus, ut tristique sem neque et lacus.</p>

    <svg class="hex" style="left:92px;top:476px;width:60px;height:56px;color:var(--lime)"><use href="#hex-plan"/></svg>
    <div class="band" style="top:536px;height:15px;font-size:8px;line-height:15px;">Individualized Workout Programs</div>
    <p class="lorem" style="left:30px;top:557px;width:184px;">Lorem ipsum dolor sit amet, consectetur adipiscing elit. Cras pellentesque, ante vitae bibendum porttitor, tellus augue mattis lacus, ut tristique sem neque et lacus.</p>

    <svg class="hex" style="left:92px;top:597px;width:60px;height:56px;color:var(--lime)"><use href="#hex-flex"/></svg>
    <div class="band" style="top:657px;height:15px;font-size:8px;line-height:15px;">FUN Workouts Delivering Results</div>
    <p class="lorem" style="left:30px;top:678px;width:184px;">Lorem ipsum dolor sit amet, consectetur adipiscing elit. Cras pellentesque, ante vitae bibendum porttitor, tellus augue mattis lacus, ut tristique sem neque et lacus.</p>

    <svg class="hex" style="left:92px;top:716px;width:60px;height:56px;color:var(--lime)"><use href="#hex-scale"/></svg>
    <div class="band" style="top:777px;height:15px;font-size:8px;line-height:15px;">Turn ON Fat Burning "EPOC" After Burn</div>
    <p class="lorem" style="left:30px;top:798px;width:184px;">Lorem ipsum dolor sit amet, consectetur adipiscing elit. Cras pellentesque, ante vitae bibendum porttitor, tellus augue mattis lacus, ut tristique sem neque et lacus.</p>

    <div class="contact-ico" style="left:78px;top:853px;width:36px;font-size:5px;"><svg width="12" height="14" style="color:#222"><use href="#ico-pin"/></svg><br>FIND US</div>
    <div class="contact-ico" style="left:120px;top:855px;width:42px;font-size:5px;"><svg width="16" height="12" style="color:#222"><use href="#ico-mail"/></svg><br>E-MAIL US</div>

    <div class="footer" style="top:891px;height:47px;padding-top:12px;font-size:4.8px;">© 2017 peakstride.com, LLC. All rights reserved.<br>peakstride.com is a trademark of peakstride.com, LLC.<br>© peakstride.com, 48 Harbor Ln, Seaview, FL, 32000</div>
  </section>
  <div class="device-label" style="left:743px;top:958px;width:244px;">Smartphones</div>

</main>
</body>
</html>
```